Business card for Sports Apparel business

DOUBLE SIDED DESIGN
We need business cards for a new sports apparel business. We are developing a protective headband for soccer initially.
Corvell is focused on designing and developing head protection products to reduce the likelihood of concussion when playing sports. Exploring and understanding medical insights, material science research, current and former players experiences and governing bodies guidelines has allowed Corvell to develop the safety, style, form and function requirements of a suitable product to bring to market.
Target Market(s)
Mums buying kits for the sons and daughters. Amateur footballers.
Industry/Entity Type
Sporting Good
Contact Information for Business Card
Martin Ashgrove - CEO
Mobile: +44 7391608254
Email: martin@corvell.co.uk
Tel: 0208 5143927
Helena Pardoe - COO
Mob: +44 7356 409183
Email: helena@corvell.co.uk
Tel: 0208 5143927
Duncan Wyvern - CCO
Mob: +44 7468 230517
Email: duncan@corvell.co.uk
Tel: 0208 5143927
Look and feel

```html
<!DOCTYPE html>
<html lang="en">
<head>
<meta charset="utf-8">
<title>Corvell Business Card</title>
<link href="https://fonts.googleapis.com/css2?family=Poppins:wght@400;600&display=swap" rel="stylesheet">
<style>
  :root {
    --page: #e9eaec;
    --card: #ffffff;
    --blue-deep: #2f72b3;
    --blue-light: #55bde8;
    --arc-grey: #f1f2f4;
    --ink: #4a4d52;
    --ink-soft: #7a7d82;
  }
  * { margin: 0; padding: 0; box-sizing: border-box; }
  html, body { width: 1200px; height: 800px; overflow: hidden; }
  body {
    background: var(--page);
    font-family: "Poppins", sans-serif;
    display: flex;
    align-items: center;
    justify-content: center;
    gap: 40px;
  }
  .card {
    position: relative;
    width: 540px;
    height: 310px;
    background: var(--card);
    box-shadow: 0 10px 30px rgba(0,0,0,0.12);
    overflow: hidden;
  }
  .card-art { position: absolute; inset: 0; width: 100%; height: 100%; }
  .wordmark {
    position: absolute;
    display: flex;
    align-items: center;
    gap: 8px;
    color: var(--blue-deep);
    font-weight: 600;
    letter-spacing: 2px;
    text-transform: uppercase;
  }
  .wordmark-square {
    width: 14px; height: 14px;
    background: var(--blue-deep);
  }
  .card-front .wordmark {
    font-size: 30px;
    left: 50%; top: 50%;
    transform: translate(-50%, -50%);
  }
  .card-back .wordmark {
    font-size: 24px;
    right: 70px; top: 46px;
  }
  .person {
    position: absolute;
    left: 60px; top: 140px;
  }
  .person-name {
    color: var(--blue-deep);
    font-weight: 600;
    font-size: 15px;
    text-transform: uppercase;
    letter-spacing: 0.3px;
  }
  .person-role {
    color: var(--ink-soft);
    font-size: 11px;
    margin-top: 1px;
  }
  .person-rule {
    width: 62px; height: 2px;
    background: var(--blue-deep);
    margin-top: 6px;
  }
  .contacts {
    position: absolute;
    left: 60px; top: 218px;
    list-style: none;
  }
  .contact {
    display: flex;
    align-items: center;
    gap: 10px;
    font-size: 13px;
    color: var(--ink);
    line-height: 24px;
  }
  .contact-icon {
    width: 16px; height: 16px;
    flex: none;
  }
</style>
</head>
<body>

  <section class="card card-front" aria-label="Card front">
    <svg class="card-art" viewBox="0 0 540 310" preserveAspectRatio="none" aria-hidden="true">
      <g class="swoosh-right">
        <path d="M345,0 Q450,140 540,290 L540,270 Q460,140 385,0 Z" fill="var(--arc-grey)"/>
        <path d="M395,0 Q480,110 540,235 L540,0 Z" fill="var(--blue-light)"/>
        <path d="M440,0 Q500,90 540,175 L540,0 Z" fill="var(--blue-deep)"/>
      </g>
      <g class="swoosh-left" transform="rotate(180 270 155)">
        <path d="M345,0 Q450,140 540,290 L540,270 Q460,140 385,0 Z" fill="var(--arc-grey)"/>
        <path d="M395,0 Q480,110 540,235 L540,0 Z" fill="var(--blue-light)"/>
        <path d="M440,0 Q500,90 540,175 L540,0 Z" fill="var(--blue-deep)"/>
      </g>
    </svg>
    <div class="wordmark"><span class="wordmark-square"></span>Corvell</div>
  </section>

  <section class="card card-back" aria-label="Card back">
    <svg class="card-art" viewBox="0 0 540 310" preserveAspectRatio="none" aria-hidden="true">
      <g class="swoosh-right">
        <path d="M345,0 Q450,140 540,290 L540,270 Q460,140 385,0 Z" fill="var(--arc-grey)"/>
        <path d="M395,0 Q480,110 540,235 L540,0 Z" fill="var(--blue-light)"/>
        <path d="M440,0 Q500,90 540,175 L540,0 Z" fill="var(--blue-deep)"/>
      </g>
      <path class="swoosh-corner" d="M0,225 Q50,290 150,310 L0,310 Z" fill="var(--blue-deep)"/>
    </svg>

    <div class="wordmark"><span class="wordmark-square"></span>Corvell</div>

    <div class="person">
      <p class="person-name">Martin Ashgrove</p>
      <p class="person-role">Chief Executive Officer</p>
      <div class="person-rule"></div>
    </div>

    <ul class="contacts">
      <li class="contact">
        <svg class="contact-icon" viewBox="0 0 16 16" aria-hidden="true">
          <circle cx="8" cy="8" r="8" fill="var(--blue-deep)"/>
          <rect x="5.5" y="3.5" width="5" height="9" rx="1" fill="none" stroke="#fff" stroke-width="1.1"/>
        </svg>
        +44 7391608254
      </li>
      <li class="contact">
        <svg class="contact-icon" viewBox="0 0 16 16" aria-hidden="true">
          <circle cx="8" cy="8" r="8" fill="var(--blue-deep)"/>
          <rect x="4" y="5" width="8" height="6" fill="none" stroke="#fff" stroke-width="1.1"/>
          <path d="M4,5 L8,8.5 L12,5" fill="none" stroke="#fff" stroke-width="1.1"/>
        </svg>
        martin@corvell.co.uk
      </li>
      <li class="contact">
        <svg class="contact-icon" viewBox="0 0 16 16" aria-hidden="true">
          <circle cx="8" cy="8" r="8" fill="var(--blue-deep)"/>
          <path d="M5.2,4.2 L6.8,4 L7.5,6 L6.5,6.8 Q7.3,8.6 9.2,9.5 L10,8.5 L12,9.2 L11.8,10.8 Q8.5,11.5 6,9 Q4.4,7 5.2,4.2 Z" fill="#fff"/>
        </svg>
        0208 5143927
      </li>
    </ul>
  </section>

</body>
</html>
```